Innovative approaches to treat addiction

PowerPoint on different techniques
Add graphics to screen
Easy to follow
I've provided the PowerPoint w content
Now make it pretty
And
hand outs for them to follow and take notes
Can you also add my bio:
Mara J. Trevanion, MS LCADC is a licensed Psychotherapist with a specialty in Addiction Disorders and over 22 years of clinical experience. Her integrative approach to counseling combines years of clinical experience with cognitive behavioral and traditional psychotherapy, with holistic therapies including; mindfulness, NLP, hypnotherapy, yoga therapy, reiki, motivational and wellness coaching.
Handout materials for them to follow and take notes

```html
<!DOCTYPE html>
<html lang="en">
<head>
<meta charset="utf-8">
<title>Innovative Approaches to Treat Addiction</title>
<link href="https://fonts.googleapis.com/css2?family=Questrial&display=swap" rel="stylesheet">
<style>
  :root{
    --backdrop:#3a3a3a;
    --backdrop-dark:#232323;
    --slide:#ffffff;
    --band-deep:#3d1a4a;
    --band-mid:#5b2168;
    --band-light:#7a3a86;
    --accent:#b5135f;
    --ink:#3b3b3b;
    --ink-strong:#222;
    --link:#6b6b6b;
  }
  *{box-sizing:border-box;margin:0;padding:0}
  html,body{width:1200px;height:912px;overflow:hidden}
  body{
    background:radial-gradient(circle at 50% 50%,var(--backdrop) 0%,var(--backdrop-dark) 100%);
    font-family:"Questrial",sans-serif;color:var(--ink);position:relative;
  }
  .slide{position:absolute;width:576px;height:432px;background:var(--slide);overflow:hidden;box-shadow:0 2px 8px rgba(0,0,0,.5)}
  .slide--tl{left:16px;top:16px}
  .slide--tr{left:608px;top:16px}
  .slide--bl{left:16px;top:466px}
  .slide--br{left:608px;top:466px}
  .title-band{position:absolute;left:32px;top:32px;width:512px;height:104px}
  .title-tab{position:absolute;left:488px;top:0;width:43px;height:70px;background:var(--accent)}
  .slide-title{position:absolute;left:61px;top:68px;font-size:27px;line-height:28px;color:#fff;font-weight:400;letter-spacing:.3px;white-space:nowrap}

  /* bullet points, each placed at its own line */
  .pt{position:absolute;left:82px;top:var(--y);width:var(--w,360px)}
  .pt::before{content:"";position:absolute;left:-21px;top:calc(var(--lh) / 2 - 3px);border-left:6px solid var(--accent);border-top:3px solid transparent;border-bottom:3px solid transparent}
  .pt--sub{left:103px}
  .pt--sub::before{left:-17px;border-left-width:5px}
  .pt--plain::before{display:none}
  .pt{font-size:var(--fs);line-height:var(--lh)}
  .ref{font-weight:700;color:var(--ink-strong)}
  .url{color:var(--link);text-decoration:underline}
  .visual{position:absolute}

  .med .visual{left:469px;top:160px;width:93px;height:147px;background:linear-gradient(180deg,#9ccf5a 0%,#d7ee9d 45%,#3a3a3a 60%,#c6d9a8 100%)}
  .breath .visual{left:465px;top:160px;width:97px;height:146px;background:linear-gradient(180deg,#e9ecef 0%,#d7d0cc 45%,#8a7fa3 80%,#6d5e91 100%)}
  .yoga .visual{left:460px;top:160px;width:99px;height:132px;background:linear-gradient(180deg,#eaf3f8 0%,#d9c2ae 50%,#2e6b9c 78%,#1f4e7c 100%)}
  .hyp .visual{left:454px;top:184px;width:106px;height:118px;border-radius:50%;background:radial-gradient(circle,#f1f3fb 0%,#a9b6e0 40%,#4b5fb0 62%,rgba(255,255,255,0) 72%)}
</style>
</head>
<body>

<svg width="0" height="0" style="position:absolute" aria-hidden="true">
  <defs>
    <linearGradient id="bandFill" x1="0" y1="0" x2="1" y2="0">
      <stop offset="0" stop-color="#5b2168"/>
      <stop offset=".6" stop-color="#3d1a4a"/>
      <stop offset="1" stop-color="#2f1439"/>
    </linearGradient>
    <symbol id="band" viewBox="0 0 512 104">
      <path d="M0 0H512V86C410 90 240 96 0 104Z" fill="url(#bandFill)"/>
      <path d="M0 104C240 96 410 88 512 80V88C410 91 240 98 0 104Z" fill="#7a3a86"/>
    </symbol>
  </defs>
</svg>

<!-- Meditation -->
<section class="slide slide--tl med" style="--fs:8.1px;--lh:9.6px">
  <svg class="title-band" aria-hidden="true"><use href="#band"/></svg>
  <div class="title-tab"></div>
  <h1 class="slide-title">Meditation</h1>
  <p class="pt" style="--y:153px;--w:350px">A method of achieving relaxation and consciousness by focusing on a mantras, sound, or image while eliminating outside stimuli from one's awareness.</p>
  <p class="pt" style="--y:172px;--w:370px">Mantra's- a word or phrase repeated during meditation to remain focus and calm the body</p>
  <p class="pt" style="--y:181.5px">Benefits:</p>
  <p class="pt pt--sub" style="--y:191px;--w:340px">Reduce patients physical and mental suffering, improve emotional stability and self-control, reduces mind-wandering, and improves self-care, create a calm environment</p>
  <p class="pt" style="--y:210px">Research:</p>
  <p class="pt pt--sub" style="--y:220px;--w:348px">A study conducted by Noor Halvani and colleges (2015) examined 51 adults in a meditation program. The researchers measured various states of mind wandering and evaluating them as neutral, pleasant and unpleasant topics. They also examined their caring behaviors for themselves and others. Throughout the program that lasted for nine sessions, there was a significant reduction in the participants unpleasant mind wandering, a decrease in neutral mind wandering, and a significant increase in self-care and caring behaviors for others.</p>
  <p class="pt pt--sub" style="--y:287px;--w:348px">A study was also conducted by Elena Marsh, a neuroscientist who attended Ashford Medical School, who studied the brain of long-term meditators. Marsh found an increased amount of gray matter in the insula and sensory regions as well as in the frontal cortex. Therefore, people who meditated were more mindful of their surroundings, and increased their working memory and executive decision making.</p>
  <p class="pt pt--plain ref" style="left:78px;--y:344px;--w:364px;--fs:6.6px;--lh:8.8px">Lindqvist, R. (2015). Compassion meditation reduces 'mind-wandering,' Westbrook research shows. Retrieved July 14, 2016, from <span class="url">http://news.westbrook.edu/2015/04/22/mindful-meditation-benefits-042215/</span></p>
  <p class="pt pt--plain ref" style="left:78px;--y:366px;--w:364px;--fs:6.6px;--lh:8.8px">Okafor, T. (2015). Ashford neuroscientist: Meditation not only reduces stress, here's how it changes your brain. Retrieved August 11, 2016, from https://www.dailyledger-news.com/news/inspired-life/wp/2015/05/26/ashford-neuroscientist-meditation-not-only-reduces-stress-it-literally-changes-your-brain/</p>
  <div class="visual" role="img" aria-label="Photo of stacked smooth black stones reflected in water beside a green leaf"></div>
</section>

<!-- Breathwork -->
<section class="slide slide--tr breath">
  <svg class="title-band" aria-hidden="true"><use href="#band"/></svg>
  <div class="title-tab"></div>
  <h1 class="slide-title">Breathwork</h1>
  <p class="pt" style="--y:159px;--w:362px;--fs:13.4px;--lh:12.8px">Breathwork allows the individual to disengage from negative thoughts, sensations or distractions to regain relaxation, energy and self control.</p>
  <p class="pt" style="--y:205px;--fs:9.6px;--lh:10px">Benefits:</p>
  <p class="pt pt--sub" style="--y:223px;--w:335px;--fs:11.3px;--lh:11px">Reduce the stress response which can improve the immune system and reduce the likelihood of heart disease, improve relaxation, self-control, self-esteem, prevent the relapse of reponding negatively to unwanted stimuli.</p>
  <p class="pt" style="--y:274px;--fs:9.6px;--lh:10px">Research:</p>
  <p class="pt pt--sub" style="--y:293px;--w:342px;--fs:8.6px;--lh:8.6px">Arjun Dev Sethi, PhD has conducted research which shows that with each deep breath, millions of sensory receptors in the respiratory system send signals to the brainstem which induces the parasympathetic response, by the increase of GABA levels, which results in a sense of relaxation, calmness, and mental clarity. Sethi stated that “by actively changing the breath rate it can actually change autonomic function and mood state.”</p>
  <p class="pt pt--plain ref" style="left:78px;--y:351px;--w:372px;--fs:9.2px;--lh:10.4px">Castell, M. (2015). The Science of Breathing: Discover the Breath's Power in<br>&nbsp;&nbsp;&nbsp;Yoga and Life. Retrieved July 14, 2016, from<br><span class="url">http://www.stillwaterpractice.org/article/yoga-101/science-breathing/</span></p>
  <div class="visual" role="img" aria-label="Photo of a woman seated cross-legged practicing a breathing exercise"></div>
</section>

<!-- Yoga -->
<section class="slide slide--bl yoga" style="--fs:8.6px;--lh:8.6px">
  <svg class="title-band" aria-hidden="true"><use href="#band"/></svg>
  <div class="title-tab"></div>
  <h1 class="slide-title">Yoga Asana/ Hand Mudra</h1>
  <p class="pt" style="--y:159px;--w:370px">The physical postures of yoga replaces negative thinking and behaviors with physical movement and positive thinking.</p>
  <p class="pt" style="--y:183px;--w:360px">Hand Mudra's- are positions of the body, in most cases the hand, that allows for a change in mood or energy.</p>
  <p class="pt" style="--y:224px">Benefits:</p>
  <p class="pt pt--sub" style="--y:241px;--w:340px">Allows patients to integrate mindful breathing and body awareness. Has the ability to heal an individual on every level of their being (emotional, physical, mentally and spiritually) as well as promoting a healthy lifestyle and benefiting one's overall fitness.</p>
  <p class="pt" style="--y:283px">Research:</p>
  <p class="pt pt--sub" style="--y:300px;--w:346px">Dr. Halloran an associate professor of medicine at Ashford Medical center studied yoga and concluded that yoga could be overall more beneficial to ones well being then going for a brisk walk. His research showed his clients emotionally happier (calm, confident, and in control) as well as physically more fit. “Paying attention to your breathing is important during the strength-training part of rehab. And the mindfulness and greater awareness from the meditation can help you cope with the stress of your illness, eat more healthfully, and sleep more soundly, all of which help your recovery,” she says.</p>
  <p class="pt pt--sub ref" style="--y:375px;--w:346px;--fs:8px;--lh:8.4px">Brennan, K. (2015). More than a stretch: Yoga's benefits may extend to the heart - Ashford Health Notes. Retrieved August 11, 2016, from <span class="url">http://www.health.ashford-med.org/blog/more-than-a-stretch-yogas-benefits-may-extend-to-the-heart-201504157868</span></p>
  <div class="visual" role="img" aria-label="Photo of a hand resting on a knee in a meditation mudra"></div>
</section>

<!-- Hypnosis -->
<section class="slide slide--br hyp">
  <svg class="title-band" aria-hidden="true"><use href="#band"/></svg>
  <div class="title-tab"></div>
  <h1 class="slide-title">Hypnosis/ Self Hypnosis</h1>
  <p class="pt" style="--y:157px;--w:368px;--fs:11.2px;--lh:10.8px">The practice of creating new healthy patterns through deep released concentration. Hypnosis creates an emphasis on self-care, self-love, and self-control on the patients life.</p>
  <p class="pt" style="--y:197px;--fs:13.5px;--lh:14px">Benefits:</p>
  <p class="pt pt--sub" style="--y:219px;--w:335px;--fs:10.2px;--lh:10px">Improves immune functioning, self-control, increase in relaxation, decrease in stress, reduction in recovery time, prevents relapse, decrease physical pain</p>
  <p class="pt" style="--y:257px;--fs:13.5px;--lh:14px">Research:</p>
  <p class="pt pt--sub" style="--y:279px;--w:345px;--fs:10.2px;--lh:10px">The director of integrative behavioral medicine program at Lakeview School of Medicine, Paul R. Devereux, PHD, has done extensive research on Hypnosis. HE found after a 15 minute hypnosis session prior to a surgery with 200 cancer patients. They reported less post-surgical pain, nausea, fatigue and discomfort. The hospital itself saved $772 per patient in the experiemental group since their was a reduction of the amount of time spent in surgery. Also, patients who were hypnotize required less analgesic lidocane and sedative propofol through out the surgery.</p>
  <p class="pt pt--plain" style="left:78px;--y:377px;--w:366px;--fs:6.4px;--lh:7.2px">Castell, M. (2015). The Science of Breathing: Discover the Breath's Power in Yoga and Life. Retrieved August 11, 2016, from http://www.stillwaterpractice.org/article/yoga-101/science-breathing/</p>
  <div class="visual" role="img" aria-label="Illustration of a calm figure surrounded by concentric blue hypnotic rings"></div>
</section>

</body>
</html>
```